Poetry Book Cover Design Project

Looking for a minimalistic book cover design for a collection of poems. The book title is "Before The Morning Turns To Glass". There are three parts to the book. First covers poetry in the theme of Rage. Second love and desire. The third is strange poems. Essentially the sections are "Rage", "Desire" and the "Strange". The reason for the title "Before The Morning Turns To Glass" is as if someone is writing these till life changes towards the intended outcome as felt in each poem. I want to have the author's name "Nirosha Kulathunge" at the bottom. Ilustration attached.
- Minimalistic

```html
<!DOCTYPE html>
<html lang="en">
<head>
<meta charset="utf-8">
<title>Before The Morning Turns To Glass — Nirosha Kulathunge</title>
<link rel="stylesheet" href="https://fonts.googleapis.com/css2?family=Crimson+Text:wght@400;700&display=swap">
<style>
  :root {
    --paper: #ffffff;
    --title-blue: #0b56a4;
    --author-ink: #0a0a0a;
    --cord: #555555;
    --art-red: #e23326;
    --art-red-deep: #c92b22;
  }
  html, body {
    margin: 0;
    padding: 0;
    width: 800px;
    height: 1200px;
    overflow: hidden;
    background: var(--paper);
  }
  .cover {
    position: relative;
    width: 800px;
    height: 1200px;
    background: var(--paper);
    overflow: hidden;
  }
  .hanging-cord {
    position: absolute;
    left: 214px;
    top: 0;
    width: 1px;
    height: 276px;
    background: var(--cord);
  }
  .cover-illustration {
    position: absolute;
    left: 137px;
    top: 276px;
    width: 155px;
    height: 633px;
    background: linear-gradient(to bottom, var(--art-red) 0%, var(--art-red) 80%, var(--art-red-deep) 100%);
  }
  .book-title {
    position: absolute;
    right: 68px;
    top: 43px;
    margin: 0;
    font-family: "Crimson Text", serif;
    font-weight: 400;
    font-size: 122px;
    line-height: 126px;
    color: var(--title-blue);
    text-align: right;
    letter-spacing: -1px;
  }
  .book-title span { display: block; }
  .author-name {
    position: absolute;
    left: 0;
    right: 0;
    top: 1095px;
    margin: 0;
    font-family: "Crimson Text", serif;
    font-weight: 700;
    font-size: 40px;
    line-height: 40px;
    color: var(--author-ink);
    text-align: center;
    letter-spacing: 2px;
  }
</style>
</head>
<body>
  <main class="cover">
    <div class="hanging-cord"></div>
    <div class="cover-illustration" role="img"
         aria-label="Illustration: a hanging lamp casting a tall red cone of light over a small suited figure standing beneath it"></div>

    <h1 class="book-title">
      <span>Before</span>
      <span>The</span>
      <span>Morning</span>
      <span>Turns</span>
      <span>To</span>
      <span>Glass</span>
    </h1>

    <p class="author-name">Nirosha Kulathunge</p>
  </main>
</body>
</html>
```